Korvel Professional Services Website

Small website for company presence and information. Company is an IT/Telecom services company. We provide presales and installation services. Included are various company logos including color levels. Site doesn't have to use these exact colors in the logos, but should be complimentary if using different colors. It should have a professional business appearance.
Updates

My apologies for not being more responsive on the designs that have been submitted. I will be narrowing down the submissions and providing additional feedback next week. Thank you for your patience.

Project Deadline Extended
Reason: Sorry again for delays on picking designs. Work has me very busy and I've just not had the time to devote to this project. I am extending the design deadline for a few more days to give me time to make my final decisions. Thank you all for your patience. Stay tuned....

Target Market(s)

Telecom sales companies that sell Quenti telecom products.

Industry/Entity Type

Professional Service

Coding

Coded - Design and coding required

Number of Pages Required

5+ page

Font styles to use
Sans Serif

Colors
3276b5
0355a3
85abd2
85cae6
33a6d7
0692cd
ffffff

Requirements
Must have
• Professional design reflective of IT/Telecom business. A good reference website would be: http://www.lorbextech.example/. Looking for something similar in function and presence.
Nice to have
• Rolling photos highlighting our services. Traditional navigation across the top of all pages.
Should not have
• No motion video, flashy presentation or overly confused interface.

```html
<!DOCTYPE html>
<html lang="en">
<head>
<meta charset="utf-8">
<title>Korvel Professional Services</title>
<link rel="stylesheet" href="https://fonts.googleapis.com/css2?family=Maven+Pro:wght@400;500;600;700&family=Arimo:wght@400;700&display=swap">
<style>
:root{
  --navy:#1b2a5e;
  --navy-deep:#16224f;
  --blue:#3276b5;
  --blue-strong:#0355a3;
  --blue-band:#2b7cc1;
  --blue-pale:#85abd2;
  --sky:#85cae6;
  --cyan:#33a6d7;
  --azure:#0692cd;
  --white:#ffffff;
  --ink:#3a3f4a;
  --field:#e9ecf1;
}
*{box-sizing:border-box;margin:0;padding:0}
html,body{width:1200px;height:3203px;overflow:hidden}
body{position:relative;background:var(--white);font-family:"Arimo",Arial,sans-serif;color:var(--ink)}
.abs{position:absolute}
.heading{font-family:"Maven Pro",Arial,sans-serif;font-weight:500;font-size:50px;letter-spacing:1px;color:var(--navy);line-height:1}
.heading b{color:var(--blue);font-weight:700}

/* header */
.hero{left:0;top:0;width:1200px;height:700px;background:linear-gradient(170deg,#e9eef4 0%,#b9c5d2 35%,#8d9bac 70%,#6f7d8f 100%)}
.topbar{left:0;top:0;width:1200px;height:47px;background:linear-gradient(#2f5e9b,rgba(47,94,155,0))}
.topline{left:0;top:44px;width:1200px;height:3px;background:var(--blue)}
.mail{left:735px;top:14px;font-size:15px;color:var(--white);display:flex;align-items:center;gap:8px;white-space:nowrap}
.phone{left:935px;top:0;width:186px;height:50px;background:var(--navy);color:var(--white);font-size:21px;display:flex;align-items:center;justify-content:center;gap:10px;border-radius:0 0 6px 6px}
.brand{left:77px;top:64px;display:flex;align-items:center;gap:16px}
.brand-mark{width:64px;height:64px;background:var(--blue-strong)}
.brand-name{font-family:"Maven Pro",Arial,sans-serif;font-weight:700;font-size:52px;color:var(--navy);line-height:1;letter-spacing:1px}
.brand-sub{font-family:"Maven Pro",Arial,sans-serif;font-size:16px;color:var(--blue-strong);letter-spacing:2.5px;margin-top:2px}
.nav{top:90px;left:555px;font-family:"Maven Pro",Arial,sans-serif;font-size:17px;color:var(--blue-strong)}
.nav a{color:inherit;text-decoration:none;position:absolute;white-space:nowrap}
.nav .current{color:var(--navy)}
.search{left:1083px;top:88px}
.hero-title{left:77px;top:318px;font-family:"Maven Pro",Arial,sans-serif;font-size:47px;color:#111;letter-spacing:.5px;white-space:nowrap}
.hero-sub{left:77px;top:382px;font-size:21px;color:#111}
.arrow{width:38px;height:32px;background:var(--navy);display:flex;align-items:center;justify-content:center}

/* welcome */
.welcome-title{left:0;width:1200px;top:674px;text-align:center;font-weight:400;color:var(--blue)}
.welcome-title b{color:var(--white)}
.welcome-text{left:100px;width:1000px;top:740px;text-align:center;color:var(--white);font-size:15.5px;line-height:27.5px}

/* why */
.why-title{left:77px;top:980px}
.why-list{left:77px;top:1040px;width:530px;list-style:none}
.why-list li{position:relative;padding-left:30px;font-size:15.5px;line-height:26px;margin-bottom:10px;color:#4a4f5a}
.why-list li::before{content:"";position:absolute;left:2px;top:6px;width:14px;height:14px;background:var(--navy);clip-path:polygon(50% 0,100% 25%,100% 75%,50% 100%,0 75%,0 25%)}
.btn{background:var(--navy);color:var(--white);font-family:"Maven Pro",Arial,sans-serif;font-size:21px;display:flex;align-items:center;justify-content:center;border-radius:5px}
.why-photo{left:715px;top:980px;width:408px;height:314px;background:radial-gradient(circle at 50% 55%,#2f7fb2 0%,#173a5a 40%,#0d1b2b 100%)}

/* services */
.svc{color:var(--white)}
.svc h3{font-family:"Arimo",Arial,sans-serif;font-size:17px;font-weight:700;display:flex;align-items:center;gap:10px;margin-bottom:10px}
.svc p{font-size:17px;line-height:23px;color:#d6e7f6}
.svc.center{text-align:center}
.svc.center h3{justify-content:center}
.ico{width:22px;height:22px}

/* about */
.about-title{left:0;width:1200px;top:2066px;text-align:center}
.about-media{left:77px;top:2139px;width:416px;height:312px;background:linear-gradient(180deg,#4a5e72 0%,#2b3645 45%,#9aa5ae 85%,#c9d0d5 100%)}
.about-text{left:551px;top:2139px;width:584px;font-size:16px;line-height:26.5px;color:#4a4f5a}

/* clients */
.divider{left:300px;top:2512px;width:600px;height:10px;background:radial-gradient(ellipse at center,rgba(0,0,0,.18) 0%,rgba(0,0,0,0) 70%)}
.client-title{left:0;width:1200px;top:2555px;text-align:center}
.clients{left:230px;top:2640px;width:740px;display:flex;justify-content:space-between;align-items:center}
.client{display:flex;align-items:center;gap:10px;font-family:"Maven Pro",Arial,sans-serif;font-weight:700;font-size:26px;color:var(--navy)}
.client i{display:block;width:18px;height:18px;background:var(--blue-strong);border-radius:50%}

/* footer */
.foot-h{font-family:"Arimo",Arial,sans-serif;font-size:20px;color:var(--sky)}
.sitemap{left:77px;top:2878px}
.sitemap ul{list-style:none;margin-top:22px}
.sitemap li{font-size:14.5px;color:var(--sky);height:31px;padding-left:20px;position:relative}
.sitemap li::before{content:"";position:absolute;left:0;top:5px;width:8px;height:8px;border-radius:50%;background:var(--cyan)}
.contact{left:344px;top:2878px;width:228px}
.field{display:block;width:228px;background:var(--field);font-size:12.5px;color:#333;padding:5px 8px;margin-bottom:6px}
.send{width:228px;height:30px;background:var(--navy);color:var(--white);font-size:16px;display:flex;align-items:center;justify-content:center;letter-spacing:1px}
.touch{left:615px;top:2878px;width:260px}
.touch-row{position:absolute;left:40px;font-size:14.5px;line-height:23px;color:#d3e4f5}
.copyright{left:0;top:3139px;width:1200px;height:64px;background:var(--blue);color:#111;font-size:16px;display:flex;align-items:center;justify-content:center}
</style>
</head>
<body>

<!-- hero -->
<div class="abs hero" role="img" aria-label="City skyline with a business person holding a tablet showing a network diagram"></div>
<div class="abs topbar"></div>
<div class="abs topline"></div>
<div class="abs mail">
  <svg width="18" height="13" viewBox="0 0 18 13"><rect x=".5" y=".5" width="17" height="12" fill="none" stroke="#fff"/><path d="M.5 .5 9 7l8.5-6.5" fill="none" stroke="#fff"/></svg>
  info@korvel.example
</div>
<div class="abs phone">
  <svg width="20" height="20" viewBox="0 0 24 24"><path fill="#fff" d="M6.6 10.8a15.1 15.1 0 0 0 6.6 6.6l2.2-2.2c.3-.3.7-.4 1-.2 1.1.4 2.3.6 3.6.6.6 0 1 .4 1 1V20c0 .6-.4 1-1 1C10.6 21 3 13.4 3 4c0-.6.4-1 1-1h3.5c.6 0 1 .4 1 1 0 1.3.2 2.5.6 3.6.1.3 0 .7-.2 1z"/></svg>
  555 014 7878
</div>
<div class="abs brand">
  <div class="brand-mark"></div>
  <div>
    <div class="brand-name">KORVEL</div>
    <div class="brand-sub">PROFESSIONAL SERVICES</div>
  </div>
</div>
<nav class="abs nav">
  <svg class="abs" style="left:4px;top:-22px" width="40" height="18" viewBox="0 0 40 18"><path d="M2 16 20 3l18 13" fill="none" stroke="#1b2a5e" stroke-width="3"/></svg>
  <a class="current" style="left:0">HOME</a>
  <a style="left:88px">ABOUT US</a>
  <a style="left:209px">SERVICES</a>
  <a style="left:325px">NEWS</a>
  <a style="left:412px">CONTACT</a>
</nav>
<svg class="abs search" width="22" height="22" viewBox="0 0 22 22"><circle cx="9" cy="9" r="6.5" fill="none" stroke="#fff" stroke-width="2.5"/><path d="m14 14 6 6" stroke="#fff" stroke-width="3"/></svg>

<div class="abs hero-title">KORVEL PROFESSIONAL SERVICES</div>
<div class="abs hero-sub">Lorem Ipsum is simply text of the printing and typesetting</div>
<div class="abs arrow" style="left:9px;top:347px"><svg width="12" height="16" viewBox="0 0 12 16"><path d="M10 2 3 8l7 6" fill="none" stroke="#fff" stroke-width="3"/></svg></div>
<div class="abs arrow" style="left:1152px;top:347px"><svg width="12" height="16" viewBox="0 0 12 16"><path d="m2 2 7 6-7 6" fill="none" stroke="#fff" stroke-width="3"/></svg></div>

<!-- welcome band -->
<svg class="abs" style="left:0;top:520px" width="1200" height="405" viewBox="0 0 1200 405">
  <polygon points="0,172 600,0 1200,172 1200,405 0,405" fill="#ffffff"/>
  <polygon points="0,182 600,12 1200,172 1200,405 0,405" fill="#1b2a5e"/>
  <polygon points="565,65 600,45 635,65 635,105 600,125 565,105" fill="#3276b5"/>
  <path d="m590 355 10 8 10-8M590 364l10 8 10-8" fill="none" stroke="#33a6d7" stroke-width="2"/>
</svg>
<h1 class="abs heading welcome-title">WELCOME TO <b>KORVEL</b></h1>
<p class="abs welcome-text">Lorem Ipsum is simply dummy text of the printing and typesetting industry. Lorem Ipsum has been the industry's standard dummy text ever since the 1500s, when an unknown printer took a galley of type and scrambled it to make a type specimen book. It has survived not only five centuries, but also the leap into electronic typesetting, remaining esse - ntially unchanged. It was popularised in the 1960s with the release of Letraset sheets containing Lorem Ipsum passages, and more recently</p>

<!-- why -->
<h2 class="abs heading why-title">WHY <b>KORVEL</b></h2>
<ul class="abs why-list">
  <li>Lorem Ipsum is simply dummy text of the printing and typesetting industry. Lorem Ipsum has been the industry's standard dummy.</li>
  <li>Lorem Ipsum is simply dummy text of the printing and typesetting industry. Lorem Ipsum has been the industry's standard dummy.</li>
  <li>Lorem Ipsum is simply dummy text of the printing and typesetting industry. Lorem Ipsum has been the industry's standard dummy.</li>
</ul>
<div class="abs btn" style="left:77px;top:1238px;width:177px;height:56px">KNOW MORE</div>
<div class="abs why-photo" role="img" aria-label="Hands holding a glowing digital city network above a tablet"></div>

<!-- services band -->
<svg class="abs" style="left:0;top:1334px" width="1200" height="690" viewBox="0 0 1200 690">
  <polygon points="0,0 600,96 1200,0 1200,590 600,690 0,590" fill="#2b7cc1"/>
  <g stroke="#ffffff" stroke-width="1.5" fill="none" opacity=".85">
    <path d="M600 274V252M513 324 483 307M687 324l30-17M513 424l-30 17M687 424l30 17M600 474v22"/>
  </g>
  <polygon points="600,274 687,324 687,424 600,474 513,424 513,324" fill="#3a8bd0" stroke="#ffffff" stroke-width="3"/>
  <polygon points="600,300 664,337 664,411 600,448 536,411 536,337" fill="#85abd2" opacity=".55"/>
</svg>
<div class="abs svc center" style="left:455px;top:1485px;width:290px">
  <h3><svg class="ico" viewBox="0 0 22 22"><circle cx="11" cy="10" r="5" fill="none" stroke="#fff" stroke-width="2"/><path d="M9 17h4M11 1v3M2 10h3M17 10h3M4 3l2 2M18 3l-2 2" stroke="#fff" stroke-width="2"/></svg>Implementation</h3>
  <p>Lorem Ipsum is simply dummy text of the printing and typesetting industry.</p>
</div>
<div class="abs svc" style="left:200px;top:1587px;width:250px">
  <h3><svg class="ico" viewBox="0 0 22 22"><circle cx="11" cy="11" r="9" fill="none" stroke="#fff" stroke-width="2"/><path d="M2 11h18M11 2c-4 5-4 13 0 18M11 2c4 5 4 13 0 18" fill="none" stroke="#fff" stroke-width="1.5"/></svg>Global Support Center</h3>
  <p>Lorem Ipsum is simply dummy text of the printing and typesetting.</p>
</div>
<div class="abs svc" style="left:779px;top:1585px;width:280px">
  <h3><svg class="ico" viewBox="0 0 22 22"><path d="M2 16h8l6-8 4 2-6 9H2z" fill="none" stroke="#fff" stroke-width="2"/><path d="M14 4l4-2" stroke="#fff" stroke-width="2"/></svg>Infrastructure Cabling</h3>
  <p>Lorem Ipsum is simply dummy text of the printing and typesetting industry.</p>
</div>
<div class="abs svc" style="left:209px;top:1780px;width:250px">
  <h3><svg class="ico" viewBox="0 0 22 22"><rect x="1" y="5" width="20" height="12" rx="2" fill="#fff"/><circle cx="11" cy="11" r="3.5" fill="#2b7cc1"/></svg>PreSales</h3>
  <p>Lorem Ipsum is simply dummy text of the printing and typesetting.</p>
</div>
<div class="abs svc" style="left:779px;top:1780px;width:280px">
  <h3><svg class="ico" viewBox="0 0 22 22"><rect x="4" y="3" width="16" height="11" fill="none" stroke="#fff" stroke-width="2"/><circle cx="6" cy="15" r="2.5" fill="#fff"/><path d="M2 21c0-3 2-4 4-4s4 1 4 4" fill="#fff"/></svg>Training</h3>
  <p>Lorem Ipsum is simply dummy text of the printing and typesetting industry.</p>
</div>
<div class="abs svc center" style="left:455px;top:1852px;width:290px">
  <h3><svg class="ico" viewBox="0 0 22 22"><circle cx="11" cy="11" r="4" fill="none" stroke="#fff" stroke-width="2"/><path d="M11 1v4M11 17v4M1 11h4M17 11h4M4 4l3 3M15 15l3 3M18 4l-3 3M4 18l3-3" stroke="#fff" stroke-width="2.5"/></svg>Installation</h3>
  <p>Lorem Ipsum is simply dummy text of the printing and typesetting industry.</p>
</div>

<!-- about -->
<h2 class="abs heading about-title">ABOUT <b>KORVEL</b></h2>
<div class="abs about-media" role="img" aria-label="Corridor of data center server racks with a video play button">
  <svg style="position:absolute;left:176px;top:124px" width="64" height="64" viewBox="0 0 64 64"><circle cx="32" cy="32" r="30" fill="rgba(255,255,255,.15)" stroke="#fff" stroke-width="2"/><path d="M26 20v24l19-12z" fill="#fff"/></svg>
</div>
<p class="abs about-text">Lorem Ipsum is simply dummy text of the printing and typesetting industry. Lorem Ipsum has been the industry's standard dummy text ever since the 1500s, when an unknown printer took a galley of type and scrambled it to make a type specimen book. It has survived not only five centuries, but also the leap into electronic typesetting, remaining essentially unchanged. It was popularised in the 1960s with the release of Letraset sheets containing Lorem Ipsum passages, and more recently with desktop publishing software like Aldus PageMaker including versions of Lorem Ipsum. Lorem Ipsum is simply dummy text of the printing and typesetting industry.</p>
<div class="abs btn" style="left:551px;top:2393px;width:175px;height:58px">KNOW MORE</div>

<!-- clients -->
<div class="abs divider"></div>
<h2 class="abs heading client-title">OUR <b>CLIENT</b></h2>

<!-- footer band -->
<svg class="abs" style="left:0;top:2670px" width="1200" height="470" viewBox="0 0 1200 470">
  <polygon points="0,0 600,170 1200,0 1200,470 0,470" fill="#2f86cf"/>
  <polygon points="0,14 600,186 1200,14 1200,470 0,470" fill="#0355a3"/>
  <polygon points="982,188 1089,250 1089,374 982,436 875,374 875,250" fill="none" stroke="#1b2a5e" stroke-width="26" opacity=".85"/>
</svg>
<div class="abs clients">
  <div class="client"><i></i>Teleron</div>
  <div class="client">Nexavo</div>
  <div class="client">Callvia Group</div>
  <div class="client"><i></i>Linkora</div>
</div>

<div class="abs sitemap">
  <div class="foot-h">SiteMap</div>
  <ul><li>Home</li><li>About Us</li><li>Services</li><li>News</li><li>Contact Us</li></ul>
</div>
<div class="abs contact">
  <div class="foot-h" style="margin-bottom:22px">Contact Us</div>
  <span class="field" style="height:30px">Name</span>
  <span class="field" style="height:30px">E-Mail</span>
  <span class="field" style="height:62px">Message</span>
  <div class="send">SEND</div>
</div>
<div class="abs touch">
  <div class="foot-h">Get In Touch</div>
  <svg class="abs" style="left:0;top:42px" width="22" height="24" viewBox="0 0 22 24"><path d="M11 2v20M4 6h14l3 3-3 3H4zM6 14h12" fill="none" stroke="#85cae6" stroke-width="2"/></svg>
  <div class="touch-row" style="top:42px;width:220px"><span style="color:var(--sky)">KORVEL</span><br>101 - lorem ipsum is simple dummy text of print.</div>
  <svg class="abs" style="left:2px;top:122px" width="18" height="18" viewBox="0 0 24 24"><path fill="#85cae6" d="M6.6 10.8a15.1 15.1 0 0 0 6.6 6.6l2.2-2.2c.3-.3.7-.4 1-.2 1.1.4 2.3.6 3.6.6.6 0 1 .4 1 1V20c0 .6-.4 1-1 1C10.6 21 3 13.4 3 4c0-.6.4-1 1-1h3.5c.6 0 1 .4 1 1 0 1.3.2 2.5.6 3.6.1.3 0 .7-.2 1z"/></svg>
  <div class="touch-row" style="top:119px">1-555-014-7890</div>
  <svg class="abs" style="left:2px;top:156px" width="18" height="13" viewBox="0 0 18 13"><rect width="18" height="13" fill="#85cae6"/><path d="M0 0l9 7 9-7" fill="none" stroke="#0355a3" stroke-width="1.5"/></svg>
  <div class="touch-row" style="top:151px">info@halvencloud.example</div>
  <svg class="abs" style="left:0;top:186px" width="170" height="46" viewBox="0 0 170 46">
    <polygon points="20,2 38,12 38,34 20,44 2,34 2,12" fill="#33a6d7"/>
    <polygon points="71,2 89,12 89,34 71,44 53,34 53,12" fill="none" stroke="#33a6d7" stroke-width="2"/>
    <polygon points="122,2 140,12 140,34 122,44 104,34 104,12" fill="none" stroke="#33a6d7" stroke-width="2"/>
  </svg>
</div>

<div class="abs copyright">© KORVEL PROFESSIONAL SERVICES 2017. All Rights Reserved.</div>

</body>
</html>
```